New Business Card Design Project

Updated business card design. I am moving towards more coaching of, for the most part women, who are searching for more in their lives. I am an intuitive healer, homeopath and nutritionist but also an author and motivational speaker. Int the past I have included my photo on the card but that is not essential. My book is called the Brilliance of Saffron - Reclaiming the Shade of Your Spirit so my colours are typically magenta.
Target Market(s)
Women - 35 - 60 considering improving their health. However, I am also a professional speaker with a target audience including corporate and conferences.
Industry/Entity Type
Health And Wellness
Contact Information for Business Card
Lucinda Parvell, CCH, RNCP, BSc
www.lucindaparvell.com
lucinda@lucindaparvell.com
519-362-7015
Facebook, instagram and twitter logos
Look and feel
Each slider illustrates characteristics of the customer's brand and the style your logo design should communicate.

```html
<!DOCTYPE html>
<html lang="en">
<head>
<meta charset="utf-8">
<title>Lucinda Parvell – Business Card</title>
<link rel="stylesheet" href="https://fonts.googleapis.com/css2?family=Poppins:wght@300;400;600;700&display=swap">
<style>
  :root {
    --backdrop: #2b2d31;
    --magenta: #e91e7a;
    --magenta-light: #f0408f;
    --magenta-deep: #d8186e;
    --paper: #ffffff;
    --ink: #1a1a1a;
    --ink-soft: #4a4a4a;
  }
  * { margin: 0; padding: 0; box-sizing: border-box; }
  html, body {
    width: 1200px; height: 900px; overflow: hidden;
    background: var(--backdrop);
    font-family: "Poppins", sans-serif;
  }
  .stage {
    position: relative; width: 1200px; height: 900px;
    display: flex; align-items: center; justify-content: center; gap: 60px;
  }
  .card {
    position: relative; width: 500px; height: 286px;
    border-radius: 22px; overflow: hidden;
    background: linear-gradient(135deg, var(--magenta-light) 0%, var(--magenta) 45%, var(--magenta-deep) 100%);
  }

  /* Front */
  .card-front__band {
    position: absolute; left: 0; top: 0; width: 100%; height: 128px;
    background: var(--paper);
    display: flex; flex-direction: column; align-items: center; justify-content: center;
  }
  .brand { display: flex; align-items: center; gap: 12px; }
  .brand__name {
    font-size: 34px; font-weight: 400; color: var(--ink); letter-spacing: 0.5px;
    white-space: nowrap;
  }
  .brand__dot {
    width: 30px; height: 30px; border-radius: 50%; background: var(--magenta);
  }
  .tagline {
    margin-top: 6px; font-size: 14px; font-weight: 300; color: var(--ink-soft);
    display: flex; align-items: center; gap: 8px; letter-spacing: 0.5px;
  }
  .tagline__bullet {
    width: 6px; height: 6px; border-radius: 50%; background: var(--magenta);
  }
  .card-front__info {
    position: absolute; left: 0; top: 128px; width: 100%; height: 158px;
    display: flex; align-items: center; padding: 0 30px;
  }
  .contact { color: var(--paper); flex: 1; white-space: nowrap; }
  .contact__name { font-size: 18px; font-weight: 700; line-height: 1.2; }
  .contact__credentials { font-size: 13px; font-weight: 600; margin-bottom: 8px; }
  .contact__line { font-size: 12.5px; font-weight: 300; line-height: 1.45; }
  .divider {
    width: 1.5px; height: 92px; background: var(--paper); margin: 0 26px;
  }
  .social { display: flex; gap: 16px; }
  .social__icon {
    width: 26px; height: 26px; border-radius: 50%; background: var(--paper);
  }

  /* Back */
  .card-back {
    display: flex; flex-direction: column; align-items: center; justify-content: center; gap: 14px;
  }
  .card-back__mark {
    width: 150px; height: 150px; border-radius: 50%; background: var(--paper);
  }
  .card-back__name {
    font-size: 22px; font-weight: 400; color: var(--paper); letter-spacing: 0.5px;
  }
</style>
</head>
<body>
<main class="stage">
  <section class="card card-front">
    <header class="card-front__band">
      <div class="brand">
        <span class="brand__name">Lucinda Parvell</span>
        <span class="brand__dot"></span>
      </div>
      <p class="tagline"><span class="tagline__bullet"></span>vitality pathfinder<span class="tagline__bullet"></span></p>
    </header>
    <div class="card-front__info">
      <div class="contact">
        <p class="contact__name">Lucinda Parvell</p>
        <p class="contact__credentials">CCH, RNCP, BSc</p>
        <p class="contact__line">519-362-7015</p>
        <p class="contact__line">lucinda@lucindaparvell.com</p>
        <p class="contact__line">www.lucindaparvell.com</p>
      </div>
      <span class="divider"></span>
      <div class="social" aria-label="Social media links">
        <span class="social__icon"></span>
        <span class="social__icon"></span>
        <span class="social__icon"></span>
      </div>
    </div>
  </section>

  <section class="card card-back">
    <span class="card-back__mark"></span>
    <span class="card-back__name">Lucinda Parvell</span>
  </section>
</main>
</body>
</html>
```